Online Art Gallery & Art Management Firm looking for a business card

I'm launching an online art gallery (paintings, photography, drawings, furniture, books, ...) where people can buy all types of art. It's a platform where young and unknown artists can showcase their oeuvre.

Additionally, the venture will act as my advising company for artists. I help them out with their business side of life and become their representative.

The company name: The Velvet Parlour
Logo is attached

I'm looking for something very classy and upmarket.
Updates

Reason: Logo wasn't finished yet...

The design should include the following information: - Name: Pieter Vandomme - Title: Founder - Mobile: +32 (0) 486 514 362 - E-mail: pieter@velvet-parlour.example - Website www.velvet-parlour.example I prefer the have the logo (without website) on the one side and the information on the other. Best regards Pieter

Target Market(s)

Art buyers / art dealers / artists / middle class / upmarket /

Industry/Entity Type

Artists

Colors

Designer to choose colors to be used in the design.

Requirements
Must have
• Must communicate credibility, trust and integrity
Nice to have
• Something classy, chique
Should not have
• Nothing to artistic or creative

```html
<!DOCTYPE html>
<html lang="en">
<head>
<meta charset="utf-8">
<title>The Velvet Parlour — Business Card</title>
<link href="https://fonts.googleapis.com/css2?family=Arimo:wght@400&family=Josefin+Sans:wght@300&display=swap" rel="stylesheet">
<style>
  :root {
    --page: #e4e2df;
    --card-white: #ffffff;
    --card-black: #050505;
    --ink: #111111;
    --ink-soft: #1d1d1d;
    --paper-text: #f4f4f4;
  }
  html, body {
    margin: 0;
    width: 1200px;
    height: 900px;
    overflow: hidden;
    background: var(--page);
  }
  .canvas {
    position: relative;
    width: 1200px;
    height: 900px;
    display: flex;
    flex-direction: column;
    align-items: center;
    justify-content: center;
    gap: 36px;
  }
  .card {
    position: relative;
    width: 600px;
    height: 343px;
    box-sizing: border-box;
    box-shadow: 0 6px 18px rgba(0,0,0,0.18);
  }
  .card--front { background: var(--card-white); color: var(--ink); }
  .card--back {
    background: var(--card-black);
    color: var(--paper-text);
    display: flex;
    align-items: center;
    justify-content: center;
  }
  .brand-name {
    font-family: "Josefin Sans", sans-serif;
    font-weight: 300;
    text-transform: uppercase;
    letter-spacing: 0.28em;
    margin: 0;
    white-space: nowrap;
  }
  .card--back .brand-name { font-size: 22px; }
  .card--front .brand-name {
    position: absolute;
    left: 40px;
    top: 52px;
    font-size: 19px;
  }
  .holder-name {
    position: absolute;
    right: 40px;
    top: 46px;
    margin: 0;
    font-family: "Arimo", sans-serif;
    font-size: 21px;
    font-weight: 400;
  }
  .contact-list {
    position: absolute;
    left: 40px;
    bottom: 34px;
    margin: 0;
    padding: 0;
    list-style: none;
    font-family: "Arimo", sans-serif;
    font-size: 13px;
    color: var(--ink-soft);
  }
  .contact-item {
    display: flex;
    align-items: center;
    gap: 22px;
    height: 28px;
  }
  .contact-icon { width: 18px; height: 18px; fill: var(--ink); }
</style>
</head>
<body>
  <main class="canvas">
    <section class="card card--front" aria-label="Card front">
      <p class="brand-name">The Velvet Parlour</p>
      <h1 class="holder-name">Your Name</h1>
      <ul class="contact-list">
        <li class="contact-item">
          <svg class="contact-icon" viewBox="0 0 24 24" aria-hidden="true"><path d="M6.6 10.8a15.2 15.2 0 0 0 6.6 6.6l2.2-2.2a1 1 0 0 1 1-.25 11.4 11.4 0 0 0 3.6.57 1 1 0 0 1 1 1V20a1 1 0 0 1-1 1A17 17 0 0 1 3 4a1 1 0 0 1 1-1h3.5a1 1 0 0 1 1 1c0 1.25.2 2.45.57 3.57a1 1 0 0 1-.25 1z"/></svg>
          <span>123 456 789</span>
        </li>
        <li class="contact-item">
          <svg class="contact-icon" viewBox="0 0 24 24" aria-hidden="true"><path fill-rule="evenodd" d="M12 2a10 10 0 1 0 0 20 10 10 0 0 0 0-20zm-1 2.1c-1.2 1.4-2 3.5-2.2 5.9h2.2zm2 0V10h2.2c-.2-2.4-1-4.5-2.2-5.9zM8.8 12H11v5.9c-1.2-1.4-2-3.5-2.2-5.9zm4.2 0h2.2c-.2 2.4-1 4.5-2.2 5.9zM4.1 10h2.7c.1-2 .6-3.9 1.4-5.2A8 8 0 0 0 4.1 10zm0 2a8 8 0 0 0 4.1 5.2c-.8-1.3-1.3-3.2-1.4-5.2zm13.1 0c-.1 2-.6 3.9-1.4 5.2a8 8 0 0 0 4.1-5.2zm2.7-2a8 8 0 0 0-4.1-5.2c.8 1.3 1.3 3.2 1.4 5.2z"/></svg>
          <span>www.loremipsum.example</span>
        </li>
        <li class="contact-item">
          <svg class="contact-icon" viewBox="0 0 24 24" aria-hidden="true"><path d="M2 5h20v14H2zm2 2v.4l8 5.2 8-5.2V7zm0 2.8V17h16V9.8l-8 5.2z"/></svg>
          <span>lorem@ipsum.example</span>
        </li>
      </ul>
    </section>
    <section class="card card--back" aria-label="Card back">
      <p class="brand-name">The Velvet Parlour</p>
    </section>
  </main>
</body>
</html>
```